ZEPHIRO needs a new business card!

ZEPHIRO is a group of gaming enthusiasts who are looking for a new corporate business card.

The typeface should be modern and minimalist with attention paid to spacing between the letters and the letters 'zephiro' look relative to each other.

Should clean, crisp and minimalist - looking serious overall but with slight tweaks to the letters to make them look playful...

Black on white is fine.

Details on the card should include:
-the word 'zephiro'
-a job title (use any, for e.g. founder)
-a name (e.g. Ned Falka)
-phone number
-email address

For inspiration: http://brisket.tumblevane-cdn.example/wp-content/uploads/2013/07/mela-1.jpg

Target Market(s)

Video gaming enthusiasts

Industry/Entity Type

Business

Requirements
Must have
• Black letter on white background.
The word "zephiro"
Nice to have
• Maybe use a conservative font like Gibraltar or Helvetica and tweaking each letter individually.

You can insert normal job titles under the "zephiro" typeface
Should not have
• Should not be cartoony or childish fonts. No colors.

```html
<!DOCTYPE html>
<html lang="en">
<head>
<meta charset="utf-8">
<title>ZEPHIRO business card</title>
<link rel="stylesheet" href="https://fonts.googleapis.com/css2?family=Arimo:wght@400&family=Inter:wght@700&display=swap">
<style>
  :root {
    --backdrop: #1a1a1a;
    --card: #f8f8f8;
    --ink: #3a3a3a;
    --ink-soft: #555555;
    --band: #1a1a1a;
  }
  * { margin: 0; padding: 0; box-sizing: border-box; }
  html, body {
    width: 1200px;
    height: 519px;
    overflow: hidden;
    background: var(--backdrop);
  }
  .canvas {
    position: relative;
    width: 1200px;
    height: 519px;
    font-family: "Arimo", Arial, sans-serif;
  }
  .card-shape {
    position: absolute;
    left: 0;
    top: 0;
  }
  .wordmark {
    position: absolute;
    left: 353px;
    top: 292px;
    font-family: "Inter", Helvetica, sans-serif;
    font-weight: 700;
    font-size: 52px;
    letter-spacing: -2px;
    line-height: 1;
    color: var(--ink);
  }
  .identity {
    position: absolute;
    right: 350px;
    top: 184px;
    text-align: right;
    color: var(--ink);
  }
  .identity .person-name {
    font-size: 19px;
    line-height: 24px;
    letter-spacing: 0.2px;
  }
  .identity .job-title {
    font-size: 12.5px;
    line-height: 16px;
    color: var(--ink-soft);
  }
  .contact-list {
    position: absolute;
    right: 352px;
    top: 290px;
    list-style: none;
    color: var(--ink);
    font-size: 12.5px;
  }
  .contact-list li {
    display: flex;
    justify-content: flex-end;
    align-items: center;
    height: 18px;
  }
  .contact-list .icon {
    width: 14px;
    height: 14px;
    margin-left: 10px;
    flex: none;
  }
</style>
</head>
<body>
<div class="canvas">
  <svg class="card-shape" width="1200" height="519" viewBox="0 0 1200 519" aria-hidden="true">
    <path d="M315 85 H870 A18 18 0 0 1 888 103 V430 H335 A20 20 0 0 1 315 410 Z" fill="var(--card)"/>
    <rect x="315" y="395" width="573" height="16" fill="var(--band)"/>
  </svg>

  <div class="wordmark">zephiro</div>

  <div class="identity">
    <div class="person-name">NED FALKA</div>
    <div class="job-title">designation</div>
  </div>

  <ul class="contact-list">
    <li>0415 392 618
      <svg class="icon" viewBox="0 0 14 14" aria-hidden="true">
        <circle cx="7" cy="7" r="5.5" fill="none" stroke="var(--ink)" stroke-width="1.4"/>
        <path d="M5 4.5 Q4 7 6 9.5 L7.5 8.5 Q6.5 7 7 5.5 Z" fill="var(--ink)"/>
      </svg>
    </li>
    <li>Street Address #&nbsp; Suite
      <svg class="icon" viewBox="0 0 14 14" aria-hidden="true">
        <path d="M1 3 H5 L6 4.5 H12 V6 M1 3 V11.5 H11 L13 6 H3 L1 11.5" fill="none" stroke="var(--ink)" stroke-width="1.1" stroke-linejoin="round"/>
      </svg>
    </li>
    <li>hello@zephiro.example
      <svg class="icon" viewBox="0 0 14 14" aria-hidden="true">
        <rect x="1.5" y="3" width="11" height="8" fill="none" stroke="var(--ink)" stroke-width="1.1"/>
        <path d="M1.5 3 L7 7.5 L12.5 3 M1.5 11 L5.5 7 M12.5 11 L8.5 7" fill="none" stroke="var(--ink)" stroke-width="1.1"/>
      </svg>
    </li>
    <li>website : www.zephiro.example
      <svg class="icon" viewBox="0 0 14 14" aria-hidden="true">
        <circle cx="7" cy="8" r="3.5" fill="var(--ink)"/>
      </svg>
    </li>
  </ul>
</div>
</body>
</html>
```